Pin Oak Media Outdoor Advertising Corporate Stationery Design

We need a full corporate stationary design for our company Pin Oak Media. We setup and lease billboards, building wraps, trailer ads and construction hoardings.

We need to establish our branding and our newly created logo. All our brand identity should point towards our values, vision and mission.

We are open to fresh new ideas for our stationary design as long as it ultimately reflects the brand & logo.

Corporate Stationary List:
1. Business Card Design
2. Letterhead Design
3. Email Signature Design
4. “Advertise Here” Design (for placement on empty billboards, etc)

All designs must include our logo and be kept simple, modern, friendly and effective.

All designs should please be provided in Illustrator, Photoshop and InDesign file formats.

More details are attached in Word.

Hey

The project has been guaranteed. We like what has been submitted so far but we''d like to see a few concepts for the "Advertise Here" design for open billboards please.

Thanks!

Target Market(s)

Male and female, corporates, business owners, media buying agencies, government & all age groups.

Industry/Entity Type

Construction

Requirements
Must have
• All designs must incorporate our colours: Pantone 319C, 320C, 321C & Hexachrome Black C.

1.Business Card Design
a. Logo
b. Name
c. Mobile
d. Landline
e. Website
f. Facebook
g. Twitter
2. Letterhead Design
a. Logo
b. Mobile
c. Landline
d. Website
e. CC reg number
f. BEE level 4 contributor
g. PRTVA member
h. Postal Address
3. Email Signature Design
a. Logo
b. Name
c. Mobile
d. Landline
e. BEE level 4 contributor
f. PRTVA member
g. Website
h. Facebook
i. Twitter
4. “Advertise Here” Design (for placement on empty billboards, etc) Majority ratio of 2:1 (eg 6m wide by 3m high) - Please use 2 attached photos.
a. Logo .co.za
b. Contact Mirela
c. Mobile
Nice to have
• Come up with a cool slogan / tagline for Business Cards, “Advertise Here” Design

```html
<!DOCTYPE html>
<html lang="en">
<head>
<meta charset="utf-8">
<title>Pin Oak Media – Advertise Here Billboard</title>
<link rel="stylesheet" href="https://fonts.googleapis.com/css2?family=Barlow+Semi+Condensed:wght@400;600;700;800&display=swap">
<style>
  :root {
    --page-bg: #e9eeee;
    --teal-mid: #88cfd3;
    --teal-light: #cde9ea;
    --teal-deep: #17838f;
    --white: #ffffff;
    --black: #111111;
  }
  html, body {
    margin: 0;
    width: 1200px;
    height: 950px;
    overflow: hidden;
    background: var(--page-bg);
    font-family: "Barlow Semi Condensed", "Arial Narrow", sans-serif;
  }
  .billboard {
    position: absolute;
    left: 120px;
    top: 255px;
    width: 960px;
    height: 440px;
    overflow: hidden;
    box-shadow: 0 10px 30px rgba(0,0,0,0.12);
  }
  .billboard__art {
    position: absolute;
    inset: 0;
    width: 960px;
    height: 440px;
  }
  .headline {
    font-family: "Barlow Semi Condensed", "Arial Narrow", sans-serif;
    font-size: 74px;
    letter-spacing: -1px;
  }
  .headline__lead {
    font-weight: 800;
    fill: var(--black);
  }
  .headline__accent {
    font-weight: 600;
    fill: var(--teal-deep);
  }
  .brand {
    position: absolute;
    left: 30px;
    bottom: 28px;
    display: flex;
    align-items: center;
    gap: 12px;
  }
  .brand__mark {
    width: 30px;
    height: 30px;
    background: var(--black);
  }
  .brand__name {
    font-size: 32px;
    font-weight: 700;
    color: var(--black);
    line-height: 1;
  }
  .contact {
    position: absolute;
    left: 610px;
    top: 332px;
    color: var(--black);
  }
  .contact__label {
    font-size: 28px;
    font-weight: 700;
    color: var(--teal-deep);
    line-height: 1.1;
  }
  .contact__phone {
    display: flex;
    align-items: center;
    gap: 8px;
    font-size: 38px;
    font-weight: 600;
    line-height: 1.05;
  }
  .contact__icon {
    width: 26px;
    height: 26px;
  }
</style>
</head>
<body>
  <section class="billboard" aria-label="Advertise Here billboard">
    <svg class="billboard__art" viewBox="0 0 960 440" role="img" aria-label="Advertise Here!">
      <rect width="960" height="440" fill="var(--teal-light)"/>
      <polygon points="0,0 640,0 375,440 0,440" fill="var(--teal-mid)"/>
      <polygon points="640,0 668,0 403,440 375,440" fill="var(--white)"/>
      <g transform="rotate(-3 480 200)">
        <polygon fill="var(--white)"
          points="0,200 210,75 210,140 750,140 750,75 960,200 750,325 750,260 210,260 210,325"/>
        <text class="headline" x="480" y="200" text-anchor="middle" dominant-baseline="central">
          <tspan class="headline__lead">Advertise</tspan>
          <tspan class="headline__accent">Here!</tspan>
        </text>
      </g>
    </svg>

    <div class="brand">
      <span class="brand__mark"></span>
      <span class="brand__name">Pin Oak Media</span>
    </div>

    <div class="contact">
      <div class="contact__label">Contact Mirela:</div>
      <div class="contact__phone">
        <svg class="contact__icon" viewBox="0 0 24 24" aria-hidden="true">
          <path fill="var(--teal-deep)" d="M6.6 10.8c1.4 2.8 3.8 5.1 6.6 6.6l2.2-2.2c.3-.3.7-.4 1-.2 1.1.4 2.3.6 3.6.6.6 0 1 .4 1 1V20c0 .6-.4 1-1 1C10.6 21 3 13.4 3 4c0-.6.4-1 1-1h3.5c.6 0 1 .4 1 1 0 1.3.2 2.5.6 3.6.1.3 0 .7-.2 1z"/>
        </svg>
        <span>12 30 5566 77889</span>
      </div>
    </div>
  </section>
</body>
</html>
```